Industrial Automation company requires a business card design

Valtrin Automation provides design & build of Automated Equipment for manufacturing industry.
www.valtrinautomation.example
The equipment we design is used for manufacturing in sectors such as medical device, pharmaceutical, aerospace and electronics.
We require a new business card design which incorporates our (New) logo and the key message words:
Automated Equipment:
Design, Build, Control, Test, Support

```html
<!DOCTYPE html>
<html lang="en">
<head>
<meta charset="utf-8">
<title>Valtrin Automation – Business Card</title>
<link rel="stylesheet" href="https://fonts.googleapis.com/css2?family=Open+Sans:wght@400;600&display=swap">
<style>
  :root {
    --green: #1f8a48;
    --green-dark: #0b5a2c;
    --green-deep: #08492a;
    --ink: #4a4a4a;
    --muted: #7a7a7a;
    --paper: #ffffff;
    --stage: #2b2b2b;
    --on-green: #e6efe9;
  }
  * { margin: 0; padding: 0; box-sizing: border-box; }
  html, body { width: 1200px; height: 882px; overflow: hidden; }
  body {
    background: var(--stage);
    font-family: "Open Sans", Arial, sans-serif;
    display: flex;
    flex-direction: column;
    align-items: center;
    justify-content: center;
    gap: 36px;
  }
  .card {
    position: relative;
    width: 700px;
    height: 400px;
    border-radius: 4px;
    overflow: hidden;
  }

  /* Back */
  .card-back {
    background: linear-gradient(135deg, var(--green) 0%, var(--green-dark) 60%, var(--green-deep) 100%);
    color: var(--on-green);
    display: flex;
    flex-direction: column;
    align-items: center;
    justify-content: center;
    gap: 34px;
  }
  .card-back .brand {
    display: flex;
    align-items: center;
    gap: 14px;
    color: rgba(255,255,255,0.16);
  }
  .card-back .brand-dot {
    width: 46px; height: 46px; border-radius: 50%;
    background: rgba(255,255,255,0.16);
  }
  .card-back .brand-name {
    font-size: 40px; font-weight: 600; letter-spacing: 3px; text-transform: uppercase;
  }
  .tagline { text-align: center; font-size: 21px; line-height: 1.6; font-weight: 400; }

  /* Front */
  .card-front { background: var(--paper); color: var(--ink); }
  .card-front .brand {
    position: absolute; left: 46px; top: 52px;
    display: flex; align-items: center; gap: 12px;
  }
  .card-front .brand-dot { width: 38px; height: 38px; border-radius: 50%; background: var(--green); }
  .card-front .brand-name {
    color: var(--green); font-size: 27px; font-weight: 600; letter-spacing: 2px; text-transform: uppercase;
  }
  .person { position: absolute; right: 46px; top: 58px; text-align: right; }
  .person-name { color: var(--green); font-size: 22px; letter-spacing: 1px; text-transform: uppercase; }
  .person-title { color: var(--muted); font-size: 13px; letter-spacing: 3px; text-transform: uppercase; margin-top: 4px; }
  .contacts {
    position: absolute; right: 46px; top: 168px;
    list-style: none; font-size: 15px; line-height: 1.45; text-align: right;
  }
  .contacts li { display: flex; align-items: center; justify-content: flex-end; gap: 10px; }
  .contacts svg { width: 11px; height: 11px; fill: var(--green); flex: none; }
  .address {
    position: absolute; left: 46px; bottom: 46px;
    color: var(--green); font-size: 21px; line-height: 1.4; font-style: normal;
  }
</style>
</head>
<body>
  <section class="card card-back" aria-label="Card back">
    <div class="brand">
      <span class="brand-dot"></span>
      <span class="brand-name">Valtrin Automation</span>
    </div>
    <p class="tagline">Automated Equipment:<br>Design / Build / Control / Test / Support</p>
  </section>

  <section class="card card-front" aria-label="Card front">
    <div class="brand">
      <span class="brand-dot"></span>
      <span class="brand-name">Valtrin Automation</span>
    </div>
    <div class="person">
      <p class="person-name">Daniel R. Marsh</p>
      <p class="person-title">President</p>
    </div>
    <ul class="contacts">
      <li>888.555.0142 <svg viewBox="0 0 10 10"><rect x="2.5" y="0" width="5" height="10" rx="1"/></svg></li>
      <li>484.555.0187 <svg viewBox="0 0 10 10"><path d="M1 4 Q5 0 9 4 L8 5.5 L6.5 4.5 L6.5 3.5 Q5 3 3.5 3.5 L3.5 4.5 L2 5.5 Z M2 6 H8 V10 H2 Z"/></svg></li>
      <li>daniel@valtrinautomation.example <svg viewBox="0 0 10 10"><path d="M0 2 H10 V8 H0 Z"/></svg></li>
      <li>www.valtrinautomation.example <svg viewBox="0 0 10 10"><circle cx="5" cy="5" r="5"/></svg></li>
    </ul>
    <address class="address">Two Harbor Plaza, 18th Floor<br>Newbrook, NY 10482</address>
  </section>
</body>
</html>
```